Bakery looking for new Business cards

I have a new logo and now its time to upgrade our business cards.
e-mail - info@corwelbakehouse.com
www.corwelbakehouse.com
318-547-2096

418e Pell Creek rd. Harlow Park IL 60417
Bakehouse Hours Wednesday-Sunday 7am-4pm

Industry/Entity Type

Bakery

Contact Information for Business Card

Hr's

Requirements
Must have
• Business information.
Nice to have
• would like to include a QR code for our website.

```html
<!DOCTYPE html>
<html lang="en">
<head>
<meta charset="utf-8">
<title>Corwel Bakehouse — Business Cards</title>
<link rel="stylesheet" href="https://fonts.googleapis.com/css2?family=Montserrat:wght@400;500;700&display=swap">
<style>
  :root {
    --backdrop: #2b2b2b;
    --card: #171717;
    --gold: #e2a63b;
    --white: #ffffff;
    --soft: #e6e6e6;
  }
  * { box-sizing: border-box; margin: 0; padding: 0; }
  html, body {
    width: 1200px; height: 1200px; overflow: hidden;
    background: var(--backdrop);
    font-family: "Montserrat", sans-serif;
  }
  .sheet {
    width: 1200px; height: 1200px;
    display: flex; flex-direction: column; align-items: center; justify-content: center;
    gap: 40px;
  }
  .card {
    position: relative;
    width: 950px; height: 543px;
    background: var(--card);
    box-shadow: 0 12px 30px rgba(0,0,0,.45);
    overflow: hidden;
  }
  .card__band {
    position: absolute; left: 0; right: 0; bottom: 0;
    height: 16px; background: var(--gold);
  }
  .brand {
    display: flex; align-items: center; gap: 18px;
    color: var(--white); font-weight: 500; white-space: nowrap;
  }
  .brand__dot {
    width: 22px; height: 22px; border-radius: 50%; background: var(--gold); flex: none;
  }
  /* front */
  .front {
    display: flex; flex-direction: column; align-items: center; justify-content: flex-end;
    padding-bottom: 64px;
  }
  .front .brand { font-size: 50px; }
  .front__hours {
    margin-top: 92px;
    color: var(--soft); font-size: 19px; letter-spacing: .5px; white-space: nowrap;
  }
  /* back */
  .back { padding: 62px 0 0 80px; }
  .back .brand { font-size: 46px; }
  .back .brand__dot { width: 20px; height: 20px; }
  .person { margin-top: 52px; }
  .person__name { color: var(--gold); font-weight: 700; font-size: 34px; letter-spacing: 1px; }
  .person__role { color: var(--soft); font-size: 18px; margin-top: 2px; }
  .address { margin-top: 38px; color: var(--soft); font-size: 21px; line-height: 1.4; letter-spacing: .5px; }
  .contacts { list-style: none; margin-top: 26px; }
  .contacts li {
    display: flex; align-items: center; gap: 18px;
    color: var(--soft); font-size: 21px; letter-spacing: .5px; margin-bottom: 12px;
  }
  .contacts svg { width: 24px; height: 24px; fill: var(--gold); flex: none; }
</style>
</head>
<body>
<main class="sheet">
  <section class="card front">
    <div class="brand"><span class="brand__dot"></span>Corwel Bakehouse</div>
    <p class="front__hours">Bakehouse Hours Wednesday-Sunday 7am-4pm</p>
    <div class="card__band"></div>
  </section>

  <section class="card back">
    <div class="brand"><span class="brand__dot"></span>Corwel Bakehouse</div>
    <div class="person">
      <p class="person__name">Mara Lindqvist</p>
      <p class="person__role">Owner</p>
    </div>
    <p class="address">418e Pell Creek rd.<br>Harlow Park IL 60417</p>
    <ul class="contacts">
      <li>
        <svg viewBox="0 0 24 24" aria-hidden="true"><path d="M6.6 10.8a15.1 15.1 0 0 0 6.6 6.6l2.2-2.2a1 1 0 0 1 1-.25 11.4 11.4 0 0 0 3.6.57 1 1 0 0 1 1 1V20a1 1 0 0 1-1 1A17 17 0 0 1 3 4a1 1 0 0 1 1-1h3.5a1 1 0 0 1 1 1c0 1.25.2 2.45.57 3.57a1 1 0 0 1-.25 1z"/></svg>
        318-547-2096
      </li>
      <li>
        <svg viewBox="0 0 24 24" aria-hidden="true"><path d="M2 5h20v14H2z M3.5 6.5 12 13l8.5-6.5" fill="none" stroke="#e2a63b" stroke-width="2"/></svg>
        info@corwelbakehouse.com
      </li>
      <li>
        <svg viewBox="0 0 24 24" aria-hidden="true"><circle cx="12" cy="12" r="9" fill="none" stroke="#e2a63b" stroke-width="2"/><path d="M3 12h18M12 3c3 3 3 15 0 18M12 3c-3 3-3 15 0 18" fill="none" stroke="#e2a63b" stroke-width="1.6"/></svg>
        www.corwelbakehouse.com
      </li>
    </ul>
    <div class="card__band"></div>
  </section>
</main>
</body>
</html>
```